QUALNOVIS Process Banner

I am looking to make an ~82" x 32" stand up vertical banner that includes our companies core values, process and service delivery. I would like to be able to take these different areas and use them in other signage and print materials as well. I have attached examples of what we are looking for along with what content we already have. The content we have is very basic. Looking for some better design and creativity on how to display our core values, process and service delivery

Core Values = Do the right thing, Service Driven, Innovative, All In

Delivery Areas = Service Delivery, Centralized Services, Strategy, Automation, Technology Alignment

Our process: assessment (find a fit), proposal, onboarding, IT Roadmap, ongoing support, monitoring, maintenance

```html
<!DOCTYPE html>
<html lang="en">
<head>
<meta charset="utf-8">
<title>QUALNOVIS Process Banner</title>
<link rel="stylesheet" href="https://fonts.googleapis.com/css2?family=Archivo+Narrow:wght@400;500;700&display=swap">
<style>
  :root {
    --backdrop: #fdefdf;
    --banner: #ffffff;
    --orange: #f7941d;
    --ink: #111111;
    --swoosh: #efeff3;
    --tag-peach: #fbe0c2;
    --tag-rose: #f8c8bf;
  }
  html, body {
    margin: 0;
    padding: 0;
    width: 1200px;
    height: 1200px;
    overflow: hidden;
    background: var(--backdrop);
  }
  .canvas {
    position: relative;
    width: 1200px;
    height: 1200px;
  }
  .banner {
    position: absolute;
    left: 395px;
    top: 75px;
    width: 411px;
    height: 1050px;
    box-shadow: 0 20px 40px rgba(120, 80, 30, 0.18);
  }
  .banner svg { display: block; }
  .banner text {
    font-family: "Archivo Narrow", "Arial Narrow", sans-serif;
    fill: var(--ink);
  }
  .value-label { font-size: 12.5px; font-weight: 700; }
  .ring-title { font-size: 26px; font-weight: 700; }
  .ring-sub { font-size: 18px; font-weight: 700; }
  .section-title { font-size: 30px; font-weight: 700; }
  .area-label { font-size: 12.5px; font-weight: 700; }
  .process-title { font-size: 29px; font-weight: 700; }
  .process-step { font-size: 19.5px; font-weight: 400; }
</style>
</head>
<body>
<main class="canvas">
  <section class="banner" aria-label="QUALNOVIS process banner">
    <svg width="411" height="1050" viewBox="316 60 329 840" xmlns="http://www.w3.org/2000/svg">
      <defs>
        <clipPath id="banner-clip"><rect x="316" y="60" width="329" height="840"/></clipPath>
      </defs>
      <rect class="banner-bg" x="316" y="60" width="329" height="840" fill="var(--banner)"/>

      <g class="top-accent">
        <rect x="472" y="60" width="141" height="21" fill="var(--ink)"/>
        <rect x="478" y="60" width="141" height="16" fill="var(--orange)"/>
      </g>

      <g class="core-values" clip-path="url(#banner-clip)">
        <circle cx="354" cy="220" r="90" fill="none" stroke="var(--orange)" stroke-width="34"/>
        <text class="ring-title" x="378" y="213" text-anchor="middle">CORE</text>
        <text class="ring-sub" x="380" y="236" text-anchor="middle">VALUES</text>

        <g class="value-connectors" fill="none" stroke="var(--ink)" stroke-width="1">
          <polyline points="427,166 436,150 503,150"/>
          <line x1="441" y1="201" x2="503" y2="201"/>
          <line x1="440" y1="236" x2="503" y2="236"/>
          <polyline points="427,270 445,288 503,288"/>
        </g>
        <g class="value-nodes" fill="var(--orange)" stroke="#ffffff" stroke-width="1.5">
          <circle cx="427" cy="166" r="7"/>
          <circle cx="441" cy="201" r="7"/>
          <circle cx="440" cy="236" r="7"/>
          <circle cx="427" cy="270" r="7"/>
        </g>
        <g class="value-dots" fill="var(--ink)">
          <circle cx="503" cy="150" r="3"/>
          <circle cx="503" cy="201" r="3"/>
          <circle cx="503" cy="236" r="3"/>
          <circle cx="503" cy="288" r="3"/>
        </g>
        <text class="value-label" x="517" y="155">Do the right thing</text>
        <text class="value-label" x="517" y="208">Service Driven</text>
        <text class="value-label" x="517" y="241">Innovative</text>
        <text class="value-label" x="517" y="293">All In</text>
      </g>

      <polygon class="swoosh" points="316,432 640,287 316,462" fill="var(--swoosh)"/>

      <g class="delivery-areas">
        <text class="section-title" x="621" y="444" text-anchor="end">Delivery Areas</text>

        <text class="area-label" x="346" y="479">Centralized Services</text>
        <text class="area-label" x="531" y="479">Service Delivery</text>
        <text class="area-label" x="371" y="552">Strategy</text>
        <text class="area-label" x="542" y="552">Automation</text>
        <text class="area-label" x="499" y="605">Technology Alignment</text>

        <polygon class="flow-tag" fill="var(--tag-peach)" points="479,470 515,470 521,475.5 515,481 479,481 484,475.5"/>
        <polygon class="flow-tag" fill="var(--tag-peach)" points="575,491 587,491 587,524 581,530 575,524 575,491"/>
        <polygon class="flow-tag" fill="var(--tag-peach)" points="475,542 441,542 435,548 441,554 475,554 470,548"/>
        <polygon class="flow-tag" fill="var(--tag-rose)" points="532,542 497,542 491,548 497,554 532,554 527,548"/>
        <polygon class="flow-tag" fill="var(--tag-rose)" points="388,567 401,567 401,602 394.5,608 388,602 388,567"/>
        <polygon class="flow-tag" fill="var(--tag-peach)" points="435,596 470,596 476,602 470,608 435,608 440,602"/>
      </g>

      <rect class="divider" x="435" y="657" width="210" height="7" fill="var(--ink)"/>

      <g class="our-process">
        <rect x="316" y="665" width="329" height="235" fill="var(--orange)"/>
        <text class="process-title" x="481" y="737" text-anchor="middle">Our process:</text>
        <text class="process-step" x="481" y="762" text-anchor="middle">assessment (find a fit),</text>
        <text class="process-step" x="481" y="787" text-anchor="middle">proposal, onboarding,</text>
        <text class="process-step" x="481" y="812" text-anchor="middle">IT Roadmap, ongoing support,</text>
        <text class="process-step" x="481" y="837" text-anchor="middle">monitoring, maintenance</text>
      </g>
    </svg>
  </section>
</main>
</body>
</html>
```